Webdesign für Hersteller für Pack- und Palettieranlagen für den Getränke- und Lebensmittelbereich
Webdesign für Hersteller für Pack- und Palettieranlagen für den Getränke- und Lebensmittelbere..
Zielgruppe
Hersteller für Pack- und Palettieranlagen für den Getränke- und Lebensmittelbereich
Zielgruppe: Getränke- und Lebensmittelhersteller
Aufgabenstellung
die zukünftige Seite soll dynamischer und intuitiver werden
klare Strukturen, aber morderner als das jetztige Layout
Keine Kopie der alten Seite www.kolvand.de!
Startseite soll aufgeräumter sein
Logo, Rufnummer, Mail, Social Media
Startseite mit großem Headerbild (Slider)

```html
<!DOCTYPE html>
<html lang="de">
<head>
<meta charset="utf-8">
<title>Kolvand Maschinenbau – Pack- und Palettieranlagen</title>
<link href="https://fonts.googleapis.com/css2?family=Lexend:wght@300;400;500;600;700&display=swap" rel="stylesheet">
<style>
:root{
  --green:#6ab42d;
  --green-dark:#5a9e22;
  --orange:#e8782a;
  --ink:#333;
  --muted:#666;
  --light:#efefef;
  --dark:#464646;
  --darker:#3a3a3a;
  --white:#fff;
}
*{box-sizing:border-box;margin:0;padding:0}
html,body{width:1200px;height:3795px;overflow:hidden}
body{font-family:'Lexend',sans-serif;color:var(--ink);background:var(--white);position:relative}
.abs{position:absolute}
.section{position:absolute;left:0;width:1200px;overflow:hidden}
.section-title{position:absolute;left:0;width:1200px;text-align:center;font-size:32px;font-weight:600;letter-spacing:.5px;color:#444}
.section-title span{display:inline-block;padding:0 28px 8px;border-bottom:2px solid var(--green)}
.section-title.orange span{border-color:var(--orange)}
.btn{position:absolute;display:flex;align-items:center;justify-content:center;gap:10px;font-size:14px;font-weight:500;border-radius:4px;height:44px;width:191px}
.btn-green{background:var(--green);color:#fff}
.btn-outline{border:1.5px solid #fff;color:#fff}
.btn-outline-dark{border:1.5px solid #444;color:#444}
.chev{width:7px;height:10px}

.topbar{position:absolute;top:0;left:0;width:1200px;height:58px;background:var(--green);color:#fff;font-size:15px}
.topbar .item{position:absolute;top:19px;display:flex;align-items:center;gap:12px}
.social{position:absolute;display:flex;gap:14px}
.social i{display:block;width:15px;height:15px;border-radius:50%;background:#fff}
.nav{position:absolute;top:58px;left:0;width:1200px;height:75px;background:rgba(255,255,255,.88);z-index:2}
.brand{position:absolute;left:133px;top:26px;font-size:19px;font-weight:600;color:var(--ink);line-height:24px;letter-spacing:.3px}
.menu{position:absolute;top:31px;right:137px;display:flex;gap:43px;font-size:13.5px;font-weight:500;color:#444}
.hero{position:absolute;top:58px;left:0;width:1200px;height:666px;background:linear-gradient(110deg,#3d4238 0%,#4f6b35 40%,#6b8f3c 60%,#8a7a5a 85%,#b0906a 100%)}
.hero h1{position:absolute;left:133px;top:188px;font-size:48px;line-height:50px;font-weight:700;color:#fff;width:650px}
.hero p{position:absolute;left:133px;top:432px;width:500px;font-size:11.5px;line-height:13px;color:#fff}
.dots{position:absolute;top:642px;left:292px;display:flex;gap:25px}
.dots i{display:block;width:135px;height:2px;background:rgba(255,255,255,.3)}
.dots i.on{background:rgba(255,255,255,.8)}

.card{position:absolute;background:#fff;border-radius:10px;overflow:hidden}
.ph{display:block;width:100%}
.prod-card{top:152px;width:293px;height:331px;text-align:center}
.prod-card .ph{height:166px}
.prod-card h3{font-size:18px;font-weight:500;margin-top:17px;color:#444}
.prod-card .sub{font-size:12px;color:var(--muted);margin-top:10px;line-height:14px}
.more{font-size:14px;font-weight:500;color:var(--green);margin-top:28px;display:flex;justify-content:center;align-items:center;gap:14px}

.news{position:absolute;top:170px;width:294px}
.news .ph{height:166px;border-radius:12px}
.date{display:flex;align-items:center;gap:7px;font-size:11px;color:var(--muted)}
.news .date{margin-top:15px}
.news h4,.news-side h4{font-size:17px;font-weight:600;line-height:17px;margin-top:12px;color:#333}
.readmore{font-size:13px;font-weight:500;color:var(--orange);margin-top:14px;display:flex;align-items:center;gap:14px}
.news-side{position:absolute;left:773px;width:294px}

.job-card{top:145px;width:293px;height:231px;border-radius:12px;background:#f2f2f2;padding:22px 25px}
.job-card h4{font-size:17px;font-weight:600;margin-top:10px;color:#444}
.job-card p{font-size:12px;line-height:13px;color:#555;margin-top:20px}
.job-card .btn{left:51px;top:162px;border-radius:4px}
.job-card .outline{border:1.5px solid var(--green);color:var(--green)}

.tl-line{position:absolute;top:171px;left:240px;width:960px;border-top:2px dashed var(--green)}
.pin{position:absolute;top:155px;width:32px;height:32px;border-radius:50%;background:var(--green);border:5px solid #c6e3a8}
.pin::after{content:"";position:absolute;left:11px;top:26px;width:2px;height:30px;background:var(--green)}
.tl-card{top:228px;width:213px;height:110px;border-radius:10px;background:#fff;box-shadow:0 3px 8px rgba(0,0,0,.15);padding:16px 18px 16px 22px}
.tl-card .year{font-size:11px;font-weight:600;color:var(--green)}
.tl-card .txt{font-size:14px;font-weight:600;line-height:15px;margin-top:18px;color:#333}
.about{position:absolute;left:133px;top:391px;width:940px;font-size:14px;line-height:15px;color:#555}
.about p+p{margin-top:15px}

.lbl{position:absolute;font-size:14px;color:#555}
.field{position:absolute;background:#fff;height:32px;padding:8px 10px;font-size:14px;color:#aaa}
.bld{position:absolute;border-radius:10px;background:linear-gradient(160deg,#9fb2c2 0%,#5d7080 55%,#2f3c47 100%)}

.footer{position:absolute;top:3489px;left:0;width:1200px;height:244px;background:var(--dark);color:#eee;font-size:11px}
.footer h5{position:absolute;top:43px;font-size:12px;font-weight:600;color:#fff}
.fcol{position:absolute;top:76px;line-height:26px}
.fline{position:absolute;left:133px;line-height:13px;white-space:nowrap}
.copy{position:absolute;top:3733px;left:0;width:1200px;height:62px;background:var(--darker);color:#eee;font-size:12px;font-weight:500;text-align:center;line-height:62px}
</style>
</head>
<body>

<header class="topbar">
  <div class="item" style="left:136px">
    <svg width="15" height="15" viewBox="0 0 24 24"><path fill="#fff" d="M6.6 10.8a15 15 0 006.6 6.6l2.2-2.2c.3-.3.7-.4 1-.2 1.1.4 2.3.6 3.6.6.6 0 1 .4 1 1V20c0 .6-.4 1-1 1A17 17 0 013 4c0-.6.4-1 1-1h3.5c.6 0 1 .4 1 1 0 1.3.2 2.5.6 3.6.1.3 0 .7-.2 1z"/></svg>
    030 5550 / 412 - 0
  </div>
  <div class="item" style="left:346px">
    <svg width="17" height="13" viewBox="0 0 24 18"><path fill="#fff" d="M0 0h24v18H0z"/><path d="M1 1l11 9 11-9" stroke="#6ab42d" stroke-width="2" fill="none"/></svg>
    info@kolvand.de
  </div>
  <div class="social" style="left:958px;top:22px"><i></i><i></i><i></i><i></i></div>
</header>

<nav class="nav">
  <div class="brand">Kolvand Maschinenbau</div>
  <div class="menu"><span>PRODUKTE</span><span>AKTUELLES</span><span>JOBS / KARRIERE</span><span>ANLAGEN</span><span>UNTERNEHMEN</span></div>
</nav>

<section class="hero" role="img" aria-label="Abfüllhalle mit Förderbändern voller grüner Flaschen">
  <h1>Hersteller Für Pack-<br>Und Palettieranlagen<br>Für Den Getränke-<br>Und Lebensmittelbereich</h1>
  <p>Lorem Ipsum Dolor Sit Amet, Consectetur Adipiscing Elit, Sed Do Eiusmod Tempor Incididunt Ut Labore Et Dolore Magna Aliqua. Ut Enim Ad Minim Veniam, Quis Nostrud Exercitation Ullamco Laboris Nisi Ut Aliquip Ex Ea Commodo Consequat.</p>
  <div class="btn btn-green" style="left:133px;top:525px">Unsere Produkte</div>
  <div class="btn btn-outline" style="left:346px;top:525px">Mehr Erfahren <svg class="chev" viewBox="0 0 7 10"><path d="M1 1l4 4-4 4" stroke="#fff" stroke-width="1.5" fill="none"/></svg></div>
  <div class="dots"><i></i><i class="on"></i><i></i><i></i></div>
</section>

<section class="section" style="top:724px;height:542px;background:var(--light)">
  <h2 class="section-title" style="top:54px"><span>PRODUKTE</span></h2>
  <div class="card prod-card" style="left:133px"><div class="ph" role="img" aria-label="Gelbe Palettiermaschine" style="height:166px;background:linear-gradient(135deg,#c9b24a,#7a7f86)"></div><h3>PALETTIERTECHNIK</h3><div class="sub">VarioPal<br>Unsere Palettierfamilie</div><div class="more">Mehr Erfahren <svg class="chev" viewBox="0 0 7 10"><path d="M1 1l4 4-4 4" stroke="#6ab42d" stroke-width="1.5" fill="none"/></svg></div></div>
  <div class="card prod-card" style="left:453px"><div class="ph" role="img" aria-label="Flaschenpacker in der Produktionshalle" style="height:166px;background:linear-gradient(135deg,#8d9399,#c9b65a)"></div><h3>PACKERTECHNIK</h3><div class="sub">VarioPac<br>Unsere Flaschenpacker</div><div class="more">Mehr Erfahren <svg class="chev" viewBox="0 0 7 10"><path d="M1 1l4 4-4 4" stroke="#6ab42d" stroke-width="1.5" fill="none"/></svg></div></div>
  <div class="card prod-card" style="left:773px"><div class="ph" role="img" aria-label="Förderband mit braunen Flaschen" style="height:166px;background:linear-gradient(135deg,#a3a8ab,#5a3a28)"></div><h3>FÖRDERTECHNIK</h3><div class="sub">VarioTrans<br>Behälter- Und Gebindetransport</div><div class="more">Mehr Erfahren <svg class="chev" viewBox="0 0 7 10"><path d="M1 1l4 4-4 4" stroke="#6ab42d" stroke-width="1.5" fill="none"/></svg></div></div>
  <div class="card prod-card" style="left:1092px"><div class="ph" role="img" aria-label="Gebrauchte Anlage in einer Halle" style="height:166px;background:linear-gradient(135deg,#7b858b,#3e4a3a)"></div><h3>GEBRAUCHTMASCHINEN</h3><div class="sub">Geprüft<br>Sofort verfügbar</div><div class="more">Mehr Erfahren <svg class="chev" viewBox="0 0 7 10"><path d="M1 1l4 4-4 4" stroke="#6ab42d" stroke-width="1.5" fill="none"/></svg></div></div>
</section>

<section class="section" style="top:1266px;height:498px;background:#fff">
  <h2 class="section-title orange" style="top:60px"><span>AKTUELLES</span></h2>
  <article class="news" style="left:133px">
    <div class="ph" role="img" aria-label="Techniker mit Schutzhelm am Bedienpult" style="background:linear-gradient(135deg,#d8d8d8,#5c6670)"></div>
    <div class="date"><svg width="11" height="11" viewBox="0 0 12 12"><rect x="1" y="2" width="10" height="9" fill="none" stroke="#666"/><path d="M1 5h10" stroke="#666"/></svg>März 17, 2024</div>
    <h4>Neue Abfüllanlage für Lindtal Limo</h4>
    <div class="readmore">Weiter Lesen <svg class="chev" viewBox="0 0 7 10"><path d="M1 1l4 4-4 4" stroke="#e8782a" stroke-width="1.5" fill="none"/></svg></div>
  </article>
  <article class="news" style="left:453px">
    <div class="ph" role="img" aria-label="Roboterstraße in einer Fabrikhalle" style="background:linear-gradient(135deg,#7d8a98,#c47a3a)"></div>
    <div class="date"><svg width="11" height="11" viewBox="0 0 12 12"><rect x="1" y="2" width="10" height="9" fill="none" stroke="#666"/><path d="M1 5h10" stroke="#666"/></svg>März 17, 2024</div>
    <h4>Neue Abfüllanlage für Lindtal Limo</h4>
    <div class="readmore">Weiter Lesen <svg class="chev" viewBox="0 0 7 10"><path d="M1 1l4 4-4 4" stroke="#e8782a" stroke-width="1.5" fill="none"/></svg></div>
  </article>
  <div class="news-side" style="top:168px">
    <div class="date"><svg width="11" height="11" viewBox="0 0 12 12"><rect x="1" y="2" width="10" height="9" fill="none" stroke="#666"/><path d="M1 5h10" stroke="#666"/></svg>März 17, 2024</div>
    <h4>Neue Abfüllanlage für Lindtal Limo</h4>
  </div>
  <div class="news-side" style="top:272px">
    <div class="date"><svg width="11" height="11" viewBox="0 0 12 12"><rect x="1" y="2" width="10" height="9" fill="none" stroke="#666"/><path d="M1 5h10" stroke="#666"/></svg>März 17, 2024</div>
    <h4>Neue Abfüllanlage für Lindtal Limo</h4>
  </div>
  <div class="btn" style="left:773px;top:399px;background:#4a4a4a;color:#fff">Alle Nachrichten</div>
</section>

<section class="section" style="top:1764px;height:459px;background:linear-gradient(90deg,#5e5e5e,#6e6e6e 50%,#5a5a5a)">
  <div class="abs" role="img" aria-label="Ingenieur mit Schutzhelm und verschränkten Armen" style="left:0;top:15px;width:258px;height:444px;background:linear-gradient(180deg,#d9d9d9,#9aa3ad 60%,#7d8794);border-radius:0 120px 0 0"></div>
  <h2 class="section-title" style="top:58px;color:#fff"><span style="border-color:#fff">JOBS / KARRIERE</span></h2>
  <div class="card job-card" style="left:133px"><div class="date"><svg width="11" height="11" viewBox="0 0 12 12"><rect x="1" y="2" width="10" height="9" fill="none" stroke="#666"/><path d="M1 5h10" stroke="#666"/></svg>März 17, 2024</div><h4>Sps Progammierung</h4><p>Lorem Ipsum Dolor Sit Amet, Consectetur Adipiscing Elit, Sed Do Eiusmod Tempor Incididunt Ut Labore Et</p><div class="btn outline">Bewerben</div></div>
  <div class="card job-card" style="left:453px"><div class="date"><svg width="11" height="11" viewBox="0 0 12 12"><rect x="1" y="2" width="10" height="9" fill="none" stroke="#666"/><path d="M1 5h10" stroke="#666"/></svg>März 17, 2024</div><h4>Sps Progammierung</h4><p>Lorem Ipsum Dolor Sit Amet, Consectetur Adipiscing Elit, Sed Do Eiusmod Tempor Incididunt Ut Labore Et</p><div class="btn btn-green">Bewerben</div></div>
  <div class="card job-card" style="left:773px"><div class="date"><svg width="11" height="11" viewBox="0 0 12 12"><rect x="1" y="2" width="10" height="9" fill="none" stroke="#666"/><path d="M1 5h10" stroke="#666"/></svg>März 17, 2024</div><h4>Sps Progammierung</h4><p>Lorem Ipsum Dolor Sit Amet, Consectetur Adipiscing Elit, Sed Do Eiusmod Tempor Incididunt Ut Labore Et</p><div class="btn outline">Bewerben</div></div>
  <div class="card job-card" style="left:1092px;opacity:.5"><div class="date">März 17, 2024</div><h4>Sps Progammierung</h4><p>Lorem Ipsum Dolor Sit Amet, Consectetur Adipiscing Elit, Sed Do Eiusmod Tempor Incididunt Ut Labore Et</p><div class="btn outline">Bewerben</div></div>
</section>

<section class="section" style="top:2223px;height:640px;background:#fff">
  <h2 class="section-title" style="top:62px"><span style="border:0;padding:0">UNTERNEHMEN</span></h2>
  <div class="tl-line"></div>
  <div class="pin" style="left:223px"></div><div class="pin" style="left:463px"></div><div class="pin" style="left:703px"></div><div class="pin" style="left:943px"></div><div class="pin" style="left:1183px"></div>
  <div class="card tl-card" style="left:133px"><div class="year">1862</div><div class="txt">Gründung als FG Zeller</div></div>
  <div class="card tl-card" style="left:372px"><div class="year">1. Weltkrieg</div><div class="txt">Manuelle<br>Blechbearbeitung</div></div>
  <div class="card tl-card" style="left:612px"><div class="year">1889</div><div class="txt">Medallien auf der<br>Weltausstellung<br>in Adelaide</div></div>
  <div class="card tl-card" style="left:852px"><div class="year">Nach dem 1. Weltkrieg</div><div class="txt">Wandel zu industriellen<br>Blechbearbeitung</div></div>
  <div class="card tl-card" style="left:1092px"><div class="year">1972</div><div class="txt">Verstaatlichung</div></div>
  <div class="about">
    <p>Das Traditionsreiche Familienunternehmen Kolvand Plant, Entwickelt Und Baut Pack- Und Palettieranlagen Für Den Getränke- Und Lebensmittelbereich. Mit Erfahrung Und Know-How Planen Und Konstruieren Wir Moderne Und Effiziente Anlagen, Die Optimal Auf Die Bedürfnisse Unserer Kunden Abgestimmt Sind.</p>
    <p>Wir Bieten Ihnen Individuelle Maschinen Und Anlagen Zur Abfüllung Und Verpackung, Sortier- Und Umpackanlagen Sowie Einen Umfassenden Rundum-Service An. Mit Unseren Weitläufigen Produktionsstätten Sind Wir In Der Lage, Die Vorarbeiten Der Montage Unter Unserem Dach Zu Erledigen, Sodass Der Zeitaufwand Für Den Aufbau Bei Ihnen Vor Ort Gering Ist.</p>
  </div>
  <div class="btn btn-outline-dark" style="left:504px;top:541px">Mehr Erfahren <svg class="chev" viewBox="0 0 7 10"><path d="M1 1l4 4-4 4" stroke="#444" stroke-width="1.5" fill="none"/></svg></div>
</section>

<section class="section" style="top:2863px;height:626px;background:var(--light)">
  <h2 class="section-title" style="top:54px"><span>KONTAKT</span></h2>
  <div class="lbl" style="left:133px;top:155px">Vorname</div><div class="field" style="left:133px;top:178px;width:213px">Deine Vorname</div>
  <div class="lbl" style="left:373px;top:155px">Nachname</div><div class="field" style="left:373px;top:178px;width:213px">Deine Nachname</div>
  <div class="lbl" style="left:133px;top:244px">Email</div><div class="field" style="left:133px;top:267px;width:213px">Dein Email</div>
  <div class="lbl" style="left:373px;top:244px">Telefonnummer</div><div class="field" style="left:373px;top:267px;width:213px">Dein Telefonnummer</div>
  <div class="lbl" style="left:133px;top:333px">Vorname</div><div class="field" style="left:133px;top:356px;width:453px;height:100px">Schreibe deine Nachricht...</div>
  <div class="btn btn-green" style="left:133px;top:498px">Senden</div>
  <div class="bld" role="img" aria-label="Modernes Firmengebäude mit Glasfassade" style="left:612px;top:119px;width:214px;height:423px"></div>
  <div class="bld" role="img" aria-label="Firmengebäude Eckansicht" style="left:852px;top:119px;width:133px;height:236px"></div>
  <div class="bld" role="img" aria-label="Firmengebäude mit Eingang" style="left:852px;top:380px;width:133px;height:162px"></div>
  <div class="bld" role="img" aria-label="Werkhalle Seitenansicht" style="left:1013px;top:119px;width:200px;height:423px"></div>
</section>

<footer class="footer">
  <h5 style="left:133px">KONTAKT</h5>
  <div class="fline" style="top:76px">KOLVAND Maschinenbau GmbH</div>
  <div class="fline" style="top:89px">Am Werkhof 12</div>
  <div class="fline" style="top:102px">04720 Musterau</div>
  <div class="fline" style="top:115px">030 5550 / 412 - 0</div>
  <div class="fline" style="top:141px">030 5550 / 412 - 14</div>
  <div class="fline" style="top:167px">info@kolvand.de</div>
  <h5 style="left:412px">QUICKLINKS</h5>
  <div class="fcol" style="left:412px">Unternehmen<br>Jobs / Karriere<br>Palettiertechnik<br>Packertechnik<br>Fördertechnik</div>
  <div class="fcol" style="left:521px">Anlagen<br>Gebrauchtmaschinen<br>Aktuelles</div>
  <h5 style="left:764px">PRODUKTE</h5>
  <div class="fcol" style="left:764px">PALETTIERTECHNIK<br>PACKERTECHNIK<br>FÖRDERTECHNIK<br>GEBRAUCHTMASCHINEN</div>
  <div class="social" style="left:958px;top:153px"><i></i><i></i><i></i><i></i></div>
</footer>
<div class="copy">©2024. Kolvand All rights reserved</div>

</body>
</html>
```